Business card design for a content marketing agency

Need a business card design suitable for a digital marketing agency. Needs to be a bold and creative, high quality design that exudes expertise and professionalism, and instills in prospective new customers a sense of confidence that we are the right company to do business with. Specifications must meet PrintNorvo requirement for extra thick matte stock. Needs to incorporate logo, tagline, name, title, website url, address, city, state, zip code, and mobile number.. I spec'd s single side design but I'm to a double sided design if it's strong and compelling. I like the use of icons associated with contact info, but it's not a requirement. Mostly, the design needs to command attention because it's so good or unusual. I have all kinds of files in large thru small sizes in jpg andpgn. pick from what you need, and let me know if you have questions.

Target Market(s)

CEO, Mktg VP's and small to medium size tech and prof'l service businesses

Industry/Entity Type

Marketing

Contact Information for Business Card

Perry Lindqvist
Chief Executive Officer
418 Wexcombe Lane
Marlcombe, MA 01790
perry@quelmarketing.example
www.quelmarketing.example
978-555-2716

Font styles to use
Sans Serif

Colors
0692cd
9bcb3c

Requirements
Must have
• Tagline is "Marketing Clients Can Rely On".
• Needs to be a bold and creative, high quality design that exudes expertise and professionalism, and instills in prospective new customers a sense of confidence that we are the right company to do business with. Specifications must meet PrintNorvo requirement for extra thick matte stock. Needs to incorporate logo, tagline, name, title, website url, address, city, state, zip code, and mobile number..
Nice to have
• I spec'd s single side design but I'm open to a double sided design if it's strong and compelling. I like the use of icons associated with contact info, but it's not a requirement.
Should not have
• Chose colors that are the same and/or compatible with colors in the logo

```html
<!DOCTYPE html>
<html lang="en">
<head>
<meta charset="utf-8">
<title>Quel Digital – Business Card</title>
<link rel="stylesheet" href="https://fonts.googleapis.com/css2?family=Open+Sans:wght@400;600;700;800&display=swap">
<style>
  :root {
    --brand-blue: #0a72bd;
    --accent-blue: #1a86cf;
    --ink: #111111;
    --paper: #ffffff;
    --stage: #3a3a3c;
    --card-radius: 18px;
  }
  * { box-sizing: border-box; margin: 0; padding: 0; }
  html, body { width: 1200px; height: 900px; overflow: hidden; }
  body {
    background: var(--stage);
    font-family: "Open Sans", Arial, sans-serif;
    position: relative;
  }
  .card {
    position: absolute;
    width: 600px;
    height: 343px;
    border-radius: var(--card-radius);
    overflow: hidden;
  }

  /* Back side */
  .card-back {
    left: 70px;
    top: 80px;
    background: var(--brand-blue);
    color: var(--paper);
  }
  .card-back .brand-mark {
    position: absolute;
    right: 60px;
    top: 70px;
    display: flex;
    align-items: center;
    gap: 12px;
  }
  .card-back .brand-square {
    width: 26px; height: 26px; background: var(--paper);
  }
  .card-back .brand-name {
    font-size: 40px; font-weight: 700; letter-spacing: -0.5px; color: var(--paper);
  }
  .card-back .tagline {
    position: absolute;
    right: 50px;
    bottom: 42px;
    font-size: 13px;
    font-weight: 600;
    letter-spacing: 0.6px;
    text-transform: uppercase;
  }

  /* Front side */
  .card-front {
    left: 530px;
    top: 470px;
    background: var(--paper);
    color: var(--ink);
  }
  .card-front .edge-bands {
    position: absolute; inset: 0; width: 100%; height: 100%;
  }
  .card-front .brand-mark {
    position: absolute;
    left: 40px;
    top: 72px;
    display: flex;
    align-items: center;
    gap: 12px;
  }
  .card-front .brand-square {
    width: 22px; height: 22px; background: var(--accent-blue);
  }
  .card-front .brand-name {
    font-size: 42px; font-weight: 700; letter-spacing: -0.8px; color: var(--accent-blue);
  }
  .person {
    position: absolute;
    right: 38px;
    top: 132px;
    text-align: right;
  }
  .person-name {
    font-size: 23px; font-weight: 700; color: var(--accent-blue);
    letter-spacing: 0.5px; text-transform: uppercase; line-height: 1.05;
  }
  .person-title {
    font-size: 12.5px; font-weight: 700; text-transform: uppercase; letter-spacing: 0.2px;
  }
  .contact-list {
    position: absolute;
    right: 38px;
    top: 180px;
    list-style: none;
    text-align: right;
    font-size: 13px;
    font-weight: 600;
    line-height: 19px;
  }
  .contact-list li { display: flex; justify-content: flex-end; align-items: center; gap: 7px; }
  .contact-list svg { width: 11px; height: 11px; fill: none; stroke: var(--accent-blue); stroke-width: 2; }
  .divider {
    position: absolute;
    left: 0;
    top: 252px;
    width: 380px;
    height: 1.5px;
    background: var(--accent-blue);
  }
  .address {
    position: absolute;
    left: 55px;
    top: 264px;
    font-size: 13px;
    font-weight: 700;
    line-height: 17px;
  }
</style>
</head>
<body>

  <section class="card card-back" aria-label="Card back">
    <div class="brand-mark">
      <span class="brand-square"></span>
      <span class="brand-name">Quel Digital</span>
    </div>
    <p class="tagline">Marketing Clients Can Rely On</p>
  </section>

  <section class="card card-front" aria-label="Card front">
    <svg class="edge-bands" viewBox="0 0 600 343" preserveAspectRatio="none" aria-hidden="true">
      <polygon points="0,333 390,300 600,300 600,343 0,343" fill="#0a72bd"/>
      <polygon points="470,262 600,262 600,343 500,343 500,300 470,300" fill="#111111"/>
    </svg>

    <div class="brand-mark">
      <span class="brand-square"></span>
      <span class="brand-name">Quel Digital</span>
    </div>

    <div class="person">
      <p class="person-name">Perry Lindqvist</p>
      <p class="person-title">Chief Executive Officer</p>
    </div>

    <ul class="contact-list">
      <li>978-555-2716
        <svg viewBox="0 0 12 12"><path d="M2 1.5l2 0 1 2.5-1.3 1a6 6 0 0 0 3.3 3.3l1-1.3 2.5 1v2a1 1 0 0 1-1 1A9 9 0 0 1 1 2.5a1 1 0 0 1 1-1z"/></svg>
      </li>
      <li>perry@quelmarketing.example
        <svg viewBox="0 0 12 12"><rect x="1" y="2.5" width="10" height="7"/><path d="M1 2.5l5 4 5-4"/></svg>
      </li>
      <li>www.quelmarketing.example
        <svg viewBox="0 0 12 12"><circle cx="6" cy="6" r="5"/><path d="M1 6h10M6 1c2.5 3 2.5 7 0 10M6 1c-2.5 3-2.5 7 0 10"/></svg>
      </li>
    </ul>

    <div class="divider"></div>

    <p class="address">418 Wexcombe Lane<br>Marlcombe, MA 01790</p>
  </section>

</body>
</html>
```